ATM BUSINESS MACHINES...

NEED A NEW LOGO AND BUSINESS CARD FOR A BRAND NEW ATM BUSINESS. WE GO TO LOCAL BUSINESSES AND PLACE ATM'S IN THER STORES FOR FREE. IT INCREASES THEIR BUSINESS. A VERY EYE CATCHY LOGO AND COLOR SCHEME...MODERN, PROFESSIONAL, YET MODERN AND APPEALING....

Target Market(s)

alll types of business owners...young & old....

Industry/Entity Type

Business

Contact Information for Business Card

BRIMWELL QUICK FUNDS-ATM'S
" GET YOUR CASH NOW"
Ray T. Huxley
President/Owner
P.O. Box 87
Alder Ridge, S.V. 29318
bqf.atm@norvexmail.com
Free Atm's- Free Instalation, Free Maintenance Never a cost to business owner......Call now to get you free ATM and increase your sales......

Requirements
Nice to have
• $$$ signs.....colors....raised letters....
Maybe a logo BQF $$$ with ATM machine...

```html
<!DOCTYPE html>
<html lang="en">
<head>
<meta charset="utf-8">
<title>Brimwell Quick Funds ATM's – Business Card</title>
<link href="https://fonts.googleapis.com/css2?family=Roboto+Condensed:wght@700&family=Russo+One&display=swap" rel="stylesheet">
<style>
  :root {
    --brand-red: #d42227;
    --offer-red: #d2262b;
    --ink-dark: #0b0b0b;
    --ink-mid: #2b2b2b;
    --ink-soft: #343434;
    --white: #ffffff;
    --silver: #e3e3e3;
    --name-grey: #d6d6d6;
    --sep-light: #e6e6e6;
  }
  html, body {
    margin: 0;
    padding: 0;
    width: 1200px;
    height: 702px;
    overflow: hidden;
    background: #ffffff;
  }
  .card {
    position: relative;
    width: 1200px;
    height: 702px;
    overflow: hidden;
    background: linear-gradient(90deg, var(--ink-dark) 0%, var(--ink-mid) 55%, var(--ink-soft) 100%);
  }
  .header-band {
    position: absolute;
    left: 0; top: 0;
    width: 1200px; height: 208px;
    background: var(--brand-red);
  }
  .brand-mark {
    position: absolute;
    left: 44px; top: 44px;
    width: 142px; height: 179px;
    background: #141414;
    display: flex;
    align-items: center;
    justify-content: center;
  }
  .brand-mark-name {
    color: var(--white);
    font-family: "Roboto Condensed", "Arial Narrow", sans-serif;
    font-weight: 700;
    font-size: 50px;
  }
  .card-text {
    position: absolute;
    left: 0; top: 0;
    width: 1200px; height: 702px;
  }
  .card-text text {
    font-family: "Roboto Condensed", "Arial Narrow", sans-serif;
    font-weight: 700;
  }
  .card-text .brand-title {
    font-family: "Russo One", "Arial Black", sans-serif;
    font-weight: 400;
    font-size: 60px;
    fill: var(--silver);
  }
  .tagline { font-size: 42px; fill: var(--white); }
  .contact { font-size: 31px; fill: var(--white); }
  .person { font-size: 31px; fill: var(--name-grey); }
  .offer, .call-to-action { font-size: 31px; fill: var(--offer-red); }
</style>
</head>
<body>
  <div class="card">
    <div class="header-band"></div>

    <div class="brand-mark">
      <span class="brand-mark-name">BQF</span>
    </div>

    <svg class="card-text" width="1200" height="702" viewBox="0 0 1200 702">
      <defs>
        <linearGradient id="divider-fade" x1="0" y1="0" x2="0" y2="1">
          <stop offset="0" stop-color="#000"/>
          <stop offset="0.45" stop-color="#c2242a"/>
          <stop offset="0.55" stop-color="#c2242a"/>
          <stop offset="1" stop-color="#000"/>
        </linearGradient>
        <linearGradient id="sep-fade" x1="0" y1="0" x2="0" y2="1">
          <stop offset="0" stop-color="#e6e6e6" stop-opacity="0"/>
          <stop offset="0.5" stop-color="#e6e6e6"/>
          <stop offset="1" stop-color="#e6e6e6" stop-opacity="0"/>
        </linearGradient>
      </defs>

      <text class="brand-title" x="197" y="118" textLength="806" lengthAdjust="spacingAndGlyphs">BRIMWELL QUICK FUNDS-ATM'S</text>
      <text class="tagline" x="382" y="175" textLength="436" lengthAdjust="spacingAndGlyphs">$ GET YOUR CA$H NOW $</text>

      <text class="contact" x="330" y="376" text-anchor="middle" textLength="514" lengthAdjust="spacingAndGlyphs">P.O. Box 87 Alder Ridge, S.V. 29318</text>
      <text class="contact" x="330" y="417" text-anchor="middle">bqf.atm@norvexmail.com</text>

      <rect class="divider" x="692" y="243" width="3" height="305" fill="url(#divider-fade)"/>

      <text class="person" x="912" y="376" text-anchor="middle">Ray T. Huxley</text>
      <text class="person" x="912" y="420" text-anchor="middle">President/Owner</text>

      <text class="offer" x="24" y="609" textLength="155" lengthAdjust="spacingAndGlyphs">Free Atm's</text>
      <rect x="188" y="554" width="2" height="86" fill="url(#sep-fade)"/>
      <text class="offer" x="202" y="609" textLength="227" lengthAdjust="spacingAndGlyphs">Free Instalation</text>
      <rect x="441" y="578" width="2" height="40" fill="url(#sep-fade)"/>
      <text class="offer" x="452" y="609" textLength="259" lengthAdjust="spacingAndGlyphs">Free Maintenance</text>
      <rect x="723" y="578" width="2" height="40" fill="url(#sep-fade)"/>
      <text class="offer" x="736" y="609" textLength="439" lengthAdjust="spacingAndGlyphs">Never a cost to business owner</text>

      <text class="call-to-action" x="219" y="651" textLength="744" lengthAdjust="spacingAndGlyphs">Call now to get you free ATM and increase your sales</text>
    </svg>
  </div>
</body>
</html>
```